Here is the link where the current banner is featured https://www.brimkit.com.au/collections/gel-blasters

I need the banner recreated into desktop and mobile format size.
Update the key points to:
- FREE SHIPPING AUSTRALIA WIDE
- SAME DAY DISPATCH
- BEST PRICE GUARANTEE
- 3000+ 5 STAR REVIEWS
- BEST SERVICE & WARRANTY
- 100% SECURE CHECKOUT

I want the banner to suit the style of the website and make it look better than the last graphic.

I also need the "save even more" picture to be recreated as it looks very plain at the moment,

```html
<!DOCTYPE html>
<html lang="en">
<head>
<meta charset="utf-8">
<title>Brimkit – Gel Blasters Banners</title>
<link rel="stylesheet" href="https://fonts.googleapis.com/css2?family=Anton&family=Montserrat:wght@400;500;600;700;800;900&family=Oswald:wght@500;600&family=Roboto+Condensed:wght@400;700&display=swap">
<style>
  :root{
    --red:#e3202a;
    --red-bright:#f3262e;
    --red-deep:#d10a0a;
    --black:#0b0b0b;
    --ink:#111111;
    --white:#ffffff;
    --paper:#eceef1;
    --grey-text:#dddddd;
    --gold:#b89a62;
    --camo-a:#141414;
    --camo-b:#3b3d40;
  }
  *{box-sizing:border-box;margin:0;padding:0}
  html,body{width:1200px;height:1123px;overflow:hidden}
  body{font-family:"Montserrat",sans-serif;background:#2a2a2a}
  .canvas{position:relative;width:1200px;height:1123px;overflow:hidden;
    background:linear-gradient(100deg,#2b2b2b 0%,#5c5c5c 35%,#959595 62%,#9d9d9d 80%,#8a8a8a 100%)}
  .abs{position:absolute}

  /* promo bars */
  .promo-bar{top:0;left:0;width:1200px;height:24px;background:var(--red);display:flex;align-items:center;justify-content:center;
    font-family:"Roboto Condensed",sans-serif;font-weight:700;font-size:10px;color:var(--white)}
  .promo-bar .arrow{position:absolute;top:6px}
  .sale-bar{top:24px;left:0;width:1200px;height:39px;background:var(--red-bright)}
  .sale-bar__text{position:absolute;left:413px;top:11px;font-weight:700;font-size:15px;color:var(--white);display:flex;align-items:center;gap:4px;white-space:nowrap}
  .countdown{position:absolute;left:665px;top:10px;display:flex;align-items:flex-end;gap:2px}
  .countdown__unit{position:relative;display:flex;gap:2px}
  .countdown__label{position:absolute;top:-7px;left:0;width:100%;text-align:center;font-size:5px;color:var(--white);font-weight:500}
  .countdown__digit{width:15px;height:22px;background:var(--ink);border-radius:3px;color:var(--white);font-weight:700;font-size:16px;display:flex;align-items:center;justify-content:center}
  .countdown__sep{color:var(--white);font-weight:700;font-size:14px;height:22px;line-height:20px}

  /* camo fills */
  .camo{background:
      radial-gradient(ellipse 80px 40px at 12% 30%,var(--camo-b),transparent 70%),
      radial-gradient(ellipse 120px 50px at 45% 70%,#2a2c2f,transparent 70%),
      radial-gradient(ellipse 90px 45px at 78% 25%,var(--camo-b),transparent 70%),
      linear-gradient(180deg,#1d1e20,var(--camo-a))}
  .masthead-bg{top:63px;left:0;width:1200px;height:294px}

  /* header */
  .logo{top:84px;left:48px;font-family:"Anton",sans-serif;font-size:33px;letter-spacing:1.5px;color:var(--white);line-height:1}
  .search{top:83px;left:361px;width:477px;height:37px;background:var(--white);border-radius:3px;display:flex;align-items:center;padding-left:11px;gap:10px;font-family:"Roboto Condensed",sans-serif;font-weight:400;font-size:12px;color:#666}
  .header-tools{top:89px;left:969px;display:flex;align-items:center;color:var(--white)}
  .header-tools__phone{font-weight:800;font-size:15px;letter-spacing:-.6px;margin:0 16px 0 6px}
  .header-tools svg{display:block}

  /* navigation */
  .main-nav{top:139px;left:0;width:1200px;height:28px;background:var(--black);display:flex;align-items:center;justify-content:center;gap:22px;padding-right:85px}
  .main-nav__item{font-weight:700;font-size:12.5px;color:var(--grey-text);display:flex;align-items:center;gap:3px;letter-spacing:.2px}
  .cart-badge{top:151px;left:1143px;width:17px;height:17px;border-radius:50%;background:var(--red);border:1.5px solid var(--white);color:var(--white);font-size:7px;font-weight:700;display:flex;align-items:center;justify-content:center}

  /* perks strip */
  .perks{display:flex;gap:2.5em}
  .perk{width:13.9em;display:flex;flex-direction:column;align-items:center}
  .perk__icon{width:6em;height:5.6em;margin-bottom:1.8em;border-radius:.6em;background:linear-gradient(160deg,rgba(255,255,255,.85),rgba(255,255,255,.6))}
  .perk__label{width:100%;border:.15em solid var(--red);text-align:center;line-height:1}
  .perk__lead{background:var(--red);color:var(--white);font-weight:800;font-size:1.45em;height:1.3em;display:flex;align-items:center;justify-content:center;white-space:nowrap}
  .perk__rest{background:rgba(0,0,0,.35);color:var(--white);font-weight:500;font-size:1.35em;height:1.4em;display:flex;align-items:center;justify-content:center;white-space:nowrap;letter-spacing:0}
  .perks--header{position:absolute;top:205px;left:120px;font-size:10px}

  /* collection intro */
  .collection{top:357px;left:0;width:1200px;height:209px;background:var(--paper)}
  .collection__title{top:404px;left:43px;font-family:"Anton",sans-serif;font-size:33px;color:var(--ink);letter-spacing:.3px;line-height:1;font-weight:400}
  .collection__note{top:455px;left:43px;font-family:"Oswald",sans-serif;font-weight:500;font-size:11px;letter-spacing:1.1px;color:var(--red)}
  .control__label{font-weight:700;font-size:9px;color:var(--ink)}
  .control__select{margin-top:6px;height:35px;background:var(--white);border-radius:18px;display:flex;align-items:center;justify-content:space-between;padding:0 12px 0 17px;font-weight:500;font-size:11px;color:#333}
  .control--filter{top:418px;left:842px;width:151px}
  .control--filter .control__label{padding-left:9px}
  .control--sort{top:418px;left:1019px;width:128px}
  .control--sort .control__label{padding-left:10px}

  .product-card{top:539px;width:262px;height:27px;background:var(--white);overflow:hidden}
  .product-card__tag{position:absolute;left:0;top:0;width:40px;height:19px;background:var(--red);color:var(--white);font-weight:700;font-size:9px;display:flex;align-items:center;justify-content:center}
  .product-card__badge{position:absolute;right:0;top:9px;width:44px;height:44px;border-radius:50%;background:var(--gold)}
  .collection-fade{top:566px;left:0;width:1200px;height:1px;background:rgba(0,0,0,.15)}

  .pill-btn{display:flex;align-items:center;gap:8px;background:var(--red-bright);color:var(--white);font-weight:500;border-radius:24px;box-shadow:0 2px 6px rgba(0,0,0,.2)}
  .rewards{top:506px;left:13px;width:113px;height:46px;padding-left:17px;font-size:12px}
  .chat{top:521px;left:1103px;width:84px;height:35px;padding-left:14px;font-size:12px;gap:6px}

  /* showcase banner */
  .perk-banner{top:631px;left:98px;width:1003px;height:153px;box-shadow:0 4px 14px rgba(0,0,0,.35)}
  .perks--banner{position:absolute;top:30px;left:113px;font-size:8.1px;gap:2.42em}

  /* save more tiers */
  .tiers{position:absolute;background:var(--red-deep)}
  .tiers::before{content:"";position:absolute;left:.5em;top:.5em;right:.5em;bottom:.5em;border:.12em solid var(--white)}
  .tiers__save{position:absolute;left:.27em;top:.06em;font-family:"Anton",sans-serif;font-size:6.6em;line-height:1;color:var(--white);letter-spacing:-.01em;z-index:1}
  .tiers__flag{position:absolute;left:13.6em;top:.8em;width:11.4em;height:6.3em;background:var(--white);clip-path:polygon(14% 8%,90% 0,100% 100%,0 85%);display:flex;flex-direction:column;align-items:center;justify-content:center;padding:.2em 0 .7em 1.3em;z-index:1}
  .tiers__flag span{font-family:"Montserrat",sans-serif;font-weight:900;font-size:2.35em;line-height:.9;color:var(--red-deep);letter-spacing:-.02em}
  .tiers__rows{position:absolute;left:1.9em;top:7.3em;width:22.5em;display:flex;flex-direction:column;gap:.25em;z-index:2}
  .tier{height:1.85em;display:flex;border-radius:1em;overflow:hidden;border:.08em solid var(--white)}
  .tier__order{width:52%;background:var(--ink);color:var(--white);font-weight:700;font-size:1.15em;display:flex;align-items:center;padding-left:1.5em;line-height:1;white-space:nowrap}
  .tier__deal{flex:1;background:var(--white);color:var(--red-deep);font-weight:900;font-size:1.15em;display:flex;align-items:center;justify-content:center;border-radius:1em 0 0 1em;line-height:1;white-space:nowrap}
  .tiers--inline{top:378px;left:468px;width:263px;height:140px;font-size:10px}
  .tiers--showcase{top:835px;left:390px;width:419px;height:224px;font-size:16px;box-shadow:0 4px 16px rgba(0,0,0,.3)}
</style>
</head>
<body>
<div class="canvas">

  <div class="abs promo-bar">
    <svg class="arrow" style="left:420px" width="8" height="12" viewBox="0 0 8 12"><path d="M6 1 1 6l5 5" fill="none" stroke="#fff" stroke-width="2"/></svg>
    BEST PRICES, GUARANTEED!
    <svg class="arrow" style="left:766px" width="8" height="12" viewBox="0 0 8 12"><path d="m2 1 5 5-5 5" fill="none" stroke="#fff" stroke-width="2"/></svg>
  </div>

  <div class="abs sale-bar">
    <div class="sale-bar__text">SALE &amp; FREE SHIPPING
      <svg width="14" height="12" viewBox="0 0 14 12"><path d="M1 6h12M8 1l2 5-2 5M3 4l1 2-1 2" fill="none" stroke="#fff" stroke-width="1.8"/></svg>
      ENDS</div>
    <div class="countdown">
      <div class="countdown__unit"><span class="countdown__label">Hours</span><span class="countdown__digit">0</span><span class="countdown__digit">8</span></div>
      <span class="countdown__sep">:</span>
      <div class="countdown__unit"><span class="countdown__label">Minutes</span><span class="countdown__digit">0</span><span class="countdown__digit">4</span></div>
      <span class="countdown__sep">:</span>
      <div class="countdown__unit"><span class="countdown__label">Seconds</span><span class="countdown__digit">3</span><span class="countdown__digit">0</span></div>
    </div>
  </div>

  <div class="abs masthead-bg camo" role="img" aria-label="Dark grey camouflage pattern background"></div>

  <div class="abs logo">BRIMKIT</div>

  <div class="abs search">
    <svg width="16" height="16" viewBox="0 0 16 16"><circle cx="6.5" cy="6.5" r="5" fill="none" stroke="#111" stroke-width="1.8"/><path d="m10.5 10.5 4.5 4.5" stroke="#111" stroke-width="1.8"/></svg>
    Search
  </div>

  <div class="abs header-tools">
    <svg width="13" height="24" viewBox="0 0 13 24"><rect x="1" y="1" width="11" height="22" rx="2" fill="none" stroke="#fff" stroke-width="1.6"/><circle cx="6.5" cy="19.5" r="1" fill="#fff"/></svg>
    <span class="header-tools__phone">1300 555 019</span>
    <svg width="20" height="22" viewBox="0 0 20 22"><circle cx="10" cy="6.5" r="5" fill="none" stroke="#fff" stroke-width="1.6"/><path d="M1.5 21c0-5 4-8 8.5-8s8.5 3 8.5 8" fill="none" stroke="#fff" stroke-width="1.6"/></svg>
    <svg style="margin-left:13px" width="25" height="20" viewBox="0 0 25 20"><path d="M1 7h23l-3 12H4z" fill="none" stroke="#fff" stroke-width="1.8"/><path d="M7 7l5-6 5 6" fill="none" stroke="#fff" stroke-width="1.8"/></svg>
  </div>

  <nav class="abs main-nav">
    <span class="main-nav__item">GEL BLASTERS <svg width="9" height="6" viewBox="0 0 9 6"><path d="m1 1 3.5 3.5L8 1" fill="none" stroke="#ddd" stroke-width="1.2"/></svg></span>
    <span class="main-nav__item">GELL BALLS</span>
    <span class="main-nav__item">ACCESSORIES <svg width="9" height="6" viewBox="0 0 9 6"><path d="m1 1 3.5 3.5L8 1" fill="none" stroke="#ddd" stroke-width="1.2"/></svg></span>
    <span class="main-nav__item">TACTICAL GEAR <svg width="9" height="6" viewBox="0 0 9 6"><path d="m1 1 3.5 3.5L8 1" fill="none" stroke="#ddd" stroke-width="1.2"/></svg></span>
    <span class="main-nav__item">PARTS <svg width="9" height="6" viewBox="0 0 9 6"><path d="m1 1 3.5 3.5L8 1" fill="none" stroke="#ddd" stroke-width="1.2"/></svg></span>
    <span class="main-nav__item">NEW RELEASE</span>
  </nav>
  <div class="abs cart-badge">0</div>

  <div class="perks perks--header">
    <div class="perk"><div class="perk__icon" role="img" aria-label="Line icon of a fast-moving parcel box with Australia outline"></div><div class="perk__label"><div class="perk__lead">FREE SHIPPING</div><div class="perk__rest">AUSTRALIA WIDE</div></div></div>
    <div class="perk"><div class="perk__icon" role="img" aria-label="Line icon of a delivery truck with a clock"></div><div class="perk__label"><div class="perk__lead">SAME DAY</div><div class="perk__rest">DISPATCH</div></div></div>
    <div class="perk"><div class="perk__icon" role="img" aria-label="Line icon of a price tag with a thumbs up"></div><div class="perk__label"><div class="perk__lead">BEST PRICE</div><div class="perk__rest">GUARANTEE</div></div></div>
    <div class="perk"><div class="perk__icon" role="img" aria-label="Line icon of five-star rating bubble with a thumbs up"></div><div class="perk__label"><div class="perk__lead">3000+</div><div class="perk__rest">5 STAR REVIEWS</div></div></div>
    <div class="perk"><div class="perk__icon" role="img" aria-label="Line icon of a hand holding a shield with a tick"></div><div class="perk__label"><div class="perk__lead">BEST SERVICE</div><div class="perk__rest">&amp; WARRANTY</div></div></div>
    <div class="perk"><div class="perk__icon" role="img" aria-label="Line icon of a payment card with a security shield"></div><div class="perk__label"><div class="perk__lead">100% SECURE</div><div class="perk__rest">CHECKOUT</div></div></div>
  </div>

  <section class="abs collection"></section>
  <h1 class="abs collection__title">GEL BLASTERS</h1>
  <p class="abs collection__note">SALE LIMITED TIME ONLY + FREE SHIPPING AUSTRALIA-WIDE!</p>

  <div class="tiers tiers--inline">
    <div class="tiers__save">SAVE</div>
    <div class="tiers__flag"><span>EVEN</span><span>MORE!</span></div>
    <div class="tiers__rows">
      <div class="tier"><span class="tier__order">ORDER $250+</span><span class="tier__deal">GET 5% OFF</span></div>
      <div class="tier"><span class="tier__order">ORDER $500+</span><span class="tier__deal">GET 10% OFF</span></div>
      <div class="tier"><span class="tier__order">ORDER $1000+</span><span class="tier__deal">GET 15% OFF</span></div>
    </div>
  </div>

  <div class="abs control control--filter"><div class="control__label">FILTER BY</div><div class="control__select">All <svg width="7" height="5" viewBox="0 0 7 5"><path d="M0 0h7L3.5 5z" fill="#111"/></svg></div></div>
  <div class="abs control control--sort"><div class="control__label">SORT BY</div><div class="control__select">Featured <svg width="7" height="5" viewBox="0 0 7 5"><path d="M0 0h7L3.5 5z" fill="#111"/></svg></div></div>

  <div class="abs product-card" style="left:51px"><span class="product-card__tag" style="top:10px;height:7px"></span><span class="product-card__badge"></span></div>
  <div class="abs product-card" style="left:330px"><span class="product-card__tag">SALE</span><span class="product-card__badge"></span></div>
  <div class="abs product-card" style="left:608px"><span class="product-card__tag">SALE</span><span class="product-card__badge"></span></div>
  <div class="abs product-card" style="left:886px"><span class="product-card__tag">SALE</span><span class="product-card__badge"></span></div>

  <div class="abs pill-btn rewards">
    <svg width="22" height="20" viewBox="0 0 22 20"><path d="M2 2h8l10 10-8 7L2 10z" fill="none" stroke="#fff" stroke-width="1.8"/><circle cx="6" cy="6" r="1.4" fill="#fff"/></svg>
    Rewards
  </div>
  <div class="abs pill-btn chat">
    <svg width="16" height="16" viewBox="0 0 16 16"><path d="M8 1.5a6.5 6.5 0 1 1-3.4 12L1.5 14.5l1-3A6.5 6.5 0 0 1 8 1.5z" fill="none" stroke="#111" stroke-width="1.8"/></svg>
    Chat
  </div>

  <div class="abs collection-fade"></div>

  <div class="abs perk-banner camo" role="img" aria-label="Dark grey camouflage pattern background">
    <div class="perks perks--banner">
      <div class="perk"><div class="perk__icon" role="img" aria-label="Line icon of a fast-moving parcel box with Australia outline"></div><div class="perk__label"><div class="perk__lead">FREE SHIPPING</div><div class="perk__rest">AUSTRALIA WIDE</div></div></div>
      <div class="perk"><div class="perk__icon" role="img" aria-label="Line icon of a delivery truck with a clock"></div><div class="perk__label"><div class="perk__lead">SAME DAY</div><div class="perk__rest">DISPATCH</div></div></div>
      <div class="perk"><div class="perk__icon" role="img" aria-label="Line icon of a price tag with a thumbs up"></div><div class="perk__label"><div class="perk__lead">BEST PRICE</div><div class="perk__rest">GUARANTEE</div></div></div>
      <div class="perk"><div class="perk__icon" role="img" aria-label="Line icon of five-star rating bubble with a thumbs up"></div><div class="perk__label"><div class="perk__lead">3000+</div><div class="perk__rest">5 STAR REVIEWS</div></div></div>
      <div class="perk"><div class="perk__icon" role="img" aria-label="Line icon of a hand holding a shield with a tick"></div><div class="perk__label"><div class="perk__lead">BEST SERVICE</div><div class="perk__rest">&amp; WARRANTY</div></div></div>
      <div class="perk"><div class="perk__icon" role="img" aria-label="Line icon of a payment card with a security shield"></div><div class="perk__label"><div class="perk__lead">100% SECURE</div><div class="perk__rest">CHECKOUT</div></div></div>
    </div>
  </div>

  <div class="tiers tiers--showcase">
    <div class="tiers__save">SAVE</div>
    <div class="tiers__flag"><span>EVEN</span><span>MORE!</span></div>
    <div class="tiers__rows">
      <div class="tier"><span class="tier__order">ORDER $250+</span><span class="tier__deal">GET 5% OFF</span></div>
      <div class="tier"><span class="tier__order">ORDER $500+</span><span class="tier__deal">GET 10% OFF</span></div>
      <div class="tier"><span class="tier__order">ORDER $1000+</span><span class="tier__deal">GET 15% OFF</span></div>
    </div>
  </div>

</div>
</body>
</html>
```